Box Design of "pet rapid test for dogs & cats" with professional use

"The market is in Southeast Asia, South America, Europe, and the U.S."
Clients: Veterinary clinics, pet hospitals,(a small number of home use)

Primary colors:
Orange, Green,or Blue, (select 1,or 2 color)
Neutrals: Black, Gray, or White (optional)
Dimensions:135mm(L)*90mm(W)*105mm(W)

Kindly review the attached file for additional content
Updates

I have increased my budget, please provide a satisfactory design solution, thank you very much for your work.

Target Market(s)

Southeast Asia, South America, Europe, and the U.S.

Industry/Entity Type

Veterinary test kit for dogs & cats

Colors
0054AA
0677BA
7BADD7
CADEEF
E8F1F8
0094D4
00A9DD
6FCCEA
C7EBF8
E9F6FB
00AB8E
00BBA5
67D7C9
C6EFE9
E9F9F6
59FF00
82FF00
B8FF75
E3FFCB
F4FFEA
F0912C
F2A743
F7CA91
FBE8D2
FDF5EE
EE7325
F08F49
F5BC92
FAE3D3
FDF4ED

Requirements
Nice to have
• Appealing Box Appearance with professional

```html
<!DOCTYPE html>
<html lang="en">
<head>
<meta charset="utf-8">
<title>Pet Rapid Test Kit – Carton</title>
<link href="https://fonts.googleapis.com/css2?family=Poppins:wght@300;400;500;700;800&display=swap" rel="stylesheet">
<style>
:root{
  --teal:#5cfbe8;
  --teal-line:#48e6d4;
  --teal-soft:#8ffdf0;
  --ink:#111;
  --grey:#6f6f6f;
  --paper:#fff;
  --cut:#222;
}
*{margin:0;padding:0;box-sizing:border-box}
html,body{width:1200px;height:1200px;overflow:hidden;background:var(--paper)}
body{position:relative;font-family:"Poppins",sans-serif;color:var(--ink)}
.abs{position:absolute}
.band{position:absolute;background:var(--teal)}
.brand{position:absolute;display:flex;align-items:center;gap:.35em;color:var(--teal-line);font-weight:800;letter-spacing:.04em;white-space:nowrap}
.brand .dot{border:3px solid var(--teal-line);border-radius:50%;flex:none}
.title{font-weight:800;line-height:1.05;white-space:nowrap}
.sub{font-weight:400;white-space:nowrap}
.rule{position:absolute;height:1px;background:var(--teal-line)}
.tagline{position:absolute;display:flex;align-items:center;gap:.5em;color:var(--grey);font-weight:400;white-space:nowrap}
.plus{color:var(--teal-line);font-weight:800}
.list{position:absolute;font-weight:400;line-height:1.38}
.list ol{padding-left:1.3em}
.art{position:absolute;background:linear-gradient(160deg,#e9fffb,#bff8ef);border:1px solid var(--teal-line);border-radius:4px}
.icons{position:absolute;display:flex;align-items:center;gap:14px;color:var(--teal-line)}
.icons svg{display:block}
.count{position:absolute;font-weight:800;white-space:nowrap}
.feature{font-size:6.6px;line-height:1.35;margin-bottom:6px}
.feature b{font-weight:800;display:block;font-size:6.8px}
.feature ul{padding-left:8px}
.dieline{position:absolute;left:0;top:0}
</style>
</head>
<body>

<!-- Front panel, flat -->
<section class="front-flat">
  <div class="abs" style="left:52px;top:150px;width:478px;height:474px;border:1px solid #ddd"></div>
  <div class="band" style="left:52px;top:150px;width:478px;height:48px"></div>
  <div class="brand" style="left:84px;top:360px;font-size:18px"><span class="dot" style="width:22px;height:22px"></span>VETORA</div>
  <div class="abs title" style="left:221px;top:318px;font-size:35px">PET RAPID<br>TEST KIT</div>
  <div class="abs sub" style="left:221px;top:402px;font-size:22px">for Dogs &amp; Cats</div>
  <div class="rule" style="left:84px;top:447px;width:413px"></div>
  <div class="tagline" style="left:84px;top:455px;font-size:19px"><span class="plus" style="font-size:28px">+</span>LOVED BY PETS, TRUSTED BY VETS</div>
  <div class="list" style="left:84px;top:490px;font-size:12px">Contents<ol><li>Test Kits (Cassette,disposable dropper,desiccant).</li><li>Assay buffer</li><li>Sterile swabs.</li><li>Instruction manual.</li></ol><span style="padding-left:1.3em">Store at 2~30°C, Avoid direct sunlight</span></div>
  <div class="art" role="img" aria-label="Line illustration of a dog and a cat inside a house outline" style="left:428px;top:502px;width:68px;height:78px"></div>
  <div class="icons" style="left:84px;top:592px">
    <svg width="28" height="15"><rect x="1" y="1" width="26" height="13" fill="none" stroke="currentColor"/><text x="14" y="11" font-size="9" text-anchor="middle" fill="currentColor" font-family="Poppins,sans-serif">IVD</text></svg>
    <svg width="26" height="18"><path d="M13 1v14M9 4h8M9 15h8" stroke="currentColor" fill="none"/></svg>
    <svg width="26" height="18"><circle cx="13" cy="11" r="4" fill="none" stroke="currentColor"/><path d="M13 1v4M3 11h5M18 11h5M6 4l3 3M20 4l-3 3" stroke="currentColor"/></svg>
    <svg width="26" height="16"><path d="M1 2h11v13H1zM14 2h11v13H14z" fill="none" stroke="currentColor"/></svg>
    <svg width="18" height="18"><circle cx="9" cy="9" r="8" fill="none" stroke="currentColor"/><text x="9" y="13" font-size="11" text-anchor="middle" fill="currentColor" font-family="Poppins,sans-serif">2</text></svg>
  </div>
  <div class="count" style="left:410px;top:591px;font-size:14px">10 Tests/Box</div>
</section>

<!-- Brand mark -->
<div class="brand" style="left:790px;top:190px;font-size:58px"><span class="dot" style="width:62px;height:62px;border-width:6px"></span>VETORA</div>

<!-- Dieline -->
<section class="carton">
  <div class="band" style="left:798px;top:478px;width:320px;height:261px"></div>
  <div class="abs" style="left:860px;top:590px;width:230px;height:230px;border-radius:50%;border:10px solid var(--teal-soft);clip-path:inset(0 0 65px 0)"></div>
  <div class="brand" style="left:1012px;top:570px;font-size:11px;color:#fff"><span class="dot" style="width:14px;height:14px;border-color:#fff"></span>VETORA</div>
  <div class="band" style="left:50px;top:739px;width:1068px;height:33px"></div>
  <div class="band" style="left:50px;top:989px;width:1068px;height:155px"></div>

  <svg class="dieline" width="1200" height="1200" fill="none" stroke="var(--cut)" stroke-width=".8">
    <path d="M798 739V494q0-16 16-16h288q16 0 16 16v245"/>
    <path d="M798 526h320"/>
    <path d="M584 739v-8l6-6 8-66q2-15 18-15h176v95"/>
    <path d="M1118 741l48 6v235l-48 7"/>
    <rect x="50" y="739" width="1068" height="250"/>
    <path d="M264 739v250M584 739v250M798 739v250"/>
    <path d="M50 989l106 74v40q0 15 15 15h93V989"/>
    <path d="M264 989l72 108v30q0 17 17 17h142q17 0 17-17v-30l72-108"/>
    <path d="M798 989l-108 74v40q0 15-15 15h-91V989"/>
    <path d="M798 989v155M869 1144v-32q0-15 15-15h176q15 0 15 15v16q0 16 16 16h27V989"/>
  </svg>

  <!-- Panel: Spanish features -->
  <div class="abs" style="left:62px;top:778px;width:196px">
    <div class="feature"><b>FÁCIL Y PRÁCTICO:</b><ul><li>Sin capacitación previa</li><li>Suficientemente simple para uso en casa</li></ul></div>
    <div class="feature"><b>RÁPIDO Y EFICIENTE:</b><ul><li>Resultados digitales en &lt;10 minutos</li><li>Desde inicio hasta resultado final</li></ul></div>
    <div class="feature"><b>PRECISO Y FIABLE:</b><ul><li>Resultados rápidos y confiables con tecnología de inmunocromatografía avanzada</li><li>Validado por clínicas veterinarias a nivel global</li></ul></div>
    <div class="feature"><b>DETECCIÓN MULTIENFERMEDADES:</b><ul><li>Evalúa múltiples patologías simultáneamente</li><li>Ayudar a los dueños de mascotas a detectar problemas a tiempo</li></ul></div>
  </div>
  <div class="brand" style="left:62px;top:958px;font-size:9px"><span class="dot" style="width:12px;height:12px;border-width:2px"></span>VETORA</div>
  <div class="tagline" style="left:112px;top:967px;font-size:6.5px"><span class="plus" style="font-size:11px">+</span>LOVED BY PETS, TRUSTED BY VETS</div>

  <!-- Panel: English front -->
  <div class="brand" style="left:284px;top:812px;font-size:14px"><span class="dot" style="width:16px;height:16px"></span>VETORA</div>
  <div class="abs title" style="left:377px;top:783px;font-size:22px">PET RAPID<br>TEST KIT</div>
  <div class="abs sub" style="left:377px;top:839px;font-size:14.5px">for Dogs &amp; Cats</div>
  <div class="rule" style="left:285px;top:870px;width:278px"></div>
  <div class="tagline" style="left:285px;top:874px;font-size:12px"><span class="plus" style="font-size:17px">+</span>LOVED BY PETS, TRUSTED BY VETS</div>
  <div class="list" style="left:285px;top:898px;font-size:7.5px;line-height:1.35">Contents<ol><li>Test Kits (Cassette,disposable dropper,desiccant).</li><li>Assay buffer</li><li>Sterile swabs.</li><li>Instruction manual.</li></ol><span style="padding-left:1.3em">Store at 2~30°C, Avoid direct sunlight</span></div>
  <div class="art" role="img" aria-label="Line illustration of a dog and a cat inside a house outline" style="left:516px;top:907px;width:46px;height:52px"></div>
  <div class="icons" style="left:285px;top:969px;gap:10px;transform:scale(.62);transform-origin:left top">
    <svg width="28" height="15"><rect x="1" y="1" width="26" height="13" fill="none" stroke="currentColor"/><text x="14" y="11" font-size="9" text-anchor="middle" fill="currentColor" font-family="Poppins,sans-serif">IVD</text></svg>
    <svg width="26" height="18"><path d="M13 1v14M9 4h8M9 15h8" stroke="currentColor"/></svg>
    <svg width="26" height="18"><circle cx="13" cy="11" r="4" fill="none" stroke="currentColor"/><path d="M13 1v4M3 11h5M18 11h5" stroke="currentColor"/></svg>
    <svg width="26" height="16"><path d="M1 2h11v13H1zM14 2h11v13H14z" fill="none" stroke="currentColor"/></svg>
    <svg width="18" height="18"><circle cx="9" cy="9" r="8" fill="none" stroke="currentColor"/><text x="9" y="13" font-size="11" text-anchor="middle" fill="currentColor" font-family="Poppins,sans-serif">2</text></svg>
  </div>
  <div class="count" style="left:505px;top:967px;font-size:9px">10 Tests/Box</div>

  <!-- Panel: English side -->
  <div class="brand" style="left:596px;top:803px;font-size:10px"><span class="dot" style="width:12px;height:12px;border-width:2px"></span>VETORA</div>
  <div class="abs title" style="left:672px;top:785px;font-size:20px">PET RAPID<br>TEST KIT</div>
  <div class="abs" style="left:598px;top:851px;width:190px;font-size:7.5px;line-height:1.35">Simple &amp; Convenient:no professional skills required,Simple enough for home use.<br>Fast &amp; Efficient: Digital results in &lt; 10 minutes - from start to completion.<br>Accurate &amp; Reliable:Quick and trustworthy pet health results using advanced lateral flow biotech,Trusted by vet clinics worldwide.<br>Supports screening of multiple diseases, Helping pet owners detect issues early.</div>
  <div class="abs" style="left:598px;top:961px;font-size:6.8px;line-height:1.3;white-space:nowrap">MADE by NORVALE LABS<br>Loved by Pets, Trusted by Vets</div>
  <div class="art" role="img" aria-label="Line icons of a dog and a cat with tick marks" style="left:718px;top:950px;width:72px;height:32px"></div>

  <!-- Panel: Spanish front -->
  <div class="brand" style="left:818px;top:812px;font-size:14px"><span class="dot" style="width:16px;height:16px"></span>VETORA</div>
  <div class="abs title" style="left:912px;top:790px;font-size:17.5px">KIT DE PRUEBA RÁPIDA<br>PARA MASCOTAS</div>
  <div class="abs sub" style="left:912px;top:834px;font-size:11.5px">(Perros y Gatos)</div>
  <div class="rule" style="left:820px;top:870px;width:278px"></div>
  <div class="tagline" style="left:820px;top:874px;font-size:8px"><span class="plus" style="font-size:17px">+</span>QUERIDO POR LAS MASCOTAS, CONFIADO POR VETERINARIOS</div>
  <div class="list" style="left:820px;top:898px;font-size:7.5px;line-height:1.35">Contenido<ol><li>Kits de prueba (cassette, gotero desechable, desecante)</li><li>Buffer de ensayo</li><li>Hisopos estériles</li><li>Manual de instrucciones</li></ol><span style="padding-left:1.3em">Almacenamiento: 2~30°C</span></div>
  <div class="art" role="img" aria-label="Line illustration of a dog and a cat inside a house outline" style="left:1050px;top:907px;width:46px;height:52px"></div>
  <div class="icons" style="left:820px;top:969px;gap:10px;transform:scale(.62);transform-origin:left top">
    <svg width="28" height="15"><rect x="1" y="1" width="26" height="13" fill="none" stroke="currentColor"/><text x="14" y="11" font-size="9" text-anchor="middle" fill="currentColor" font-family="Poppins,sans-serif">IVD</text></svg>
    <svg width="26" height="18"><path d="M13 1v14M9 4h8M9 15h8" stroke="currentColor"/></svg>
    <svg width="26" height="18"><circle cx="13" cy="11" r="4" fill="none" stroke="currentColor"/><path d="M13 1v4M3 11h5M18 11h5" stroke="currentColor"/></svg>
    <svg width="26" height="16"><path d="M1 2h11v13H1zM14 2h11v13H14z" fill="none" stroke="currentColor"/></svg>
    <svg width="18" height="18"><circle cx="9" cy="9" r="8" fill="none" stroke="currentColor"/><text x="9" y="13" font-size="11" text-anchor="middle" fill="currentColor" font-family="Poppins,sans-serif">2</text></svg>
  </div>
  <div class="count" style="left:1007px;top:967px;font-size:9px">10 pruebas por caja</div>
</section>

</body>
</html>
```